Solo Law Practice Website Design

I am starting a solo law practice that will specialize in criminal defense and family law.

I have a rudimentary understanding of Wordpress as used through the hostmerry web services. The winning design would be compatible with this system so that I can modify content on my own.

I have supplied the written content and the components that I am looking for at the domain name: dorianvaskelaw.example.

I would like to take that content and work it into a website that looks more professional and inviting. The two most important goals of the website are ease of navigation and rich content for search engine spiders (for example, integrating articles into pages rather than linking to a word document).

The winning design should be turnkey for me to upload immediately.
Updates

Reason: I will be traveling.

Target Market(s)

Individuals looking for legal services.

Industry/Entity Type

Defense

Requirements
Must have
• My picture should appear at least once in the site.

The design should allow a space for me to post blog or legal updates. Additionally, there should be functionality for me to add additional articles to the site.
Nice to have
• Appropriate pictures for a legal website to break-up text on pages.

Simple flash features that won't significantly slow loading times.

Widgets that drive traffic to a contact page or function.

```html
<!DOCTYPE html>
<html lang="en">
<head>
<meta charset="utf-8">
<title>Law Offices of Dorian Vaske PLLC</title>
<link href="https://fonts.googleapis.com/css2?family=Lato:wght@300;400;700&display=swap" rel="stylesheet">
<style>
:root{
  --page:#383736;
  --white:#ffffff;
  --orange:#e8581a;
  --orange-light:#f47a32;
  --nav-active:#6b6967;
  --ink:#4a4a4a;
  --body:#8a8684;
  --band:#e9e5e0;
  --band-text:#8c7a6f;
  --rule:#9a9694;
  --footer:#65605b;
  --footer-base:#5b5651;
  --footer-text:#f2efec;
}
*{margin:0;padding:0;box-sizing:border-box}
html,body{width:686px;height:1200px;overflow:hidden}
body{background:var(--page);font-family:"Lato",Arial,sans-serif;position:relative;color:var(--ink)}
.style-switcher{position:absolute;left:5px;top:171px;display:flex;flex-direction:column;gap:6px}
.style-switcher span{width:11px;height:11px;display:block}
.site-header{position:absolute;left:69px;top:26px;width:549px;height:40px}
.brand-pre{font-size:8px;color:var(--white);letter-spacing:.3px}
.brand-name{font-size:20px;font-weight:700;color:var(--white);letter-spacing:.4px;line-height:1.1}
.brand-name em{font-style:normal;color:var(--orange)}
.header-contact{position:absolute;right:0;top:4px;font-size:8px;color:var(--white);line-height:15px}
.header-contact b{font-weight:700;margin-right:4px}
.page{position:absolute;left:69px;top:80px;width:549px;background:var(--white)}
.main-nav{height:34px;display:flex;align-items:stretch;padding-left:6px}
.main-nav a{font-size:7.7px;color:#555;text-decoration:none;display:flex;align-items:center;padding:0 6.3px}
.main-nav a.is-active{background:var(--nav-active);color:var(--white);padding:0 7.5px}
.hero{position:relative;height:229px;overflow:hidden}
.hero svg{position:absolute;inset:0}
.hero-title{position:absolute;left:325px;top:112px;color:var(--white)}
.hero-title .lead{font-size:16px;font-weight:300;letter-spacing:.3px}
.hero-title .main{font-size:20.5px;font-weight:700;line-height:21px;letter-spacing:.2px}
.tagline{height:74px;background:var(--band);display:flex;align-items:center;justify-content:center;text-align:center;font-size:16.5px;font-weight:300;color:var(--band-text);line-height:21px}
.features{display:flex;padding:22px 0 0 10px;gap:24px;height:212px}
.feature{width:160px}
.feature h2{font-size:13.5px;font-weight:400;color:var(--ink);margin-bottom:6px}
.feature .thumb{width:160px;height:75px;display:block}
.feature p{font-size:7.3px;color:var(--body);line-height:12.6px;margin-top:14px;padding-left:2px}
.content{display:flex;padding:0 12px 20px 11px;justify-content:space-between}
.areas{width:348px}
.updates{width:160px}
.section-title{font-size:13.5px;font-weight:400;color:var(--ink);padding-bottom:7px;border-bottom:1.5px solid var(--rule);margin-bottom:17px}
.area h3{font-size:11px;font-weight:400;color:var(--orange);margin-bottom:4px;padding-left:1px}
.area p{font-size:7.3px;color:var(--body);line-height:12.6px;margin-bottom:18px;padding-left:1px}
.update{margin-bottom:20px}
.update h3{font-size:10px;font-weight:400;color:var(--orange)}
.update time{display:block;font-size:6.3px;color:#444;margin:3px 0 2px}
.update p{font-size:7.3px;color:var(--body);line-height:12.6px}
.site-footer{background:var(--footer);height:171px;display:flex;padding:18px 0 0 12px;gap:25px}
.footer-col{width:158px;color:var(--footer-text)}
.footer-col h2{font-size:13px;font-weight:400;margin-bottom:10px}
.footer-col p{font-size:7.3px;line-height:12.6px}
.subscribe-form{display:flex;gap:5px;margin-top:17px}
.subscribe-form span{display:block;height:17px;font-size:6.3px;display:flex;align-items:center}
.subscribe-form .field{width:113px;background:#8b8682;color:var(--footer-text);padding-left:7px}
.subscribe-form .btn{width:40px;background:var(--orange);color:var(--white);justify-content:center}
.footer-base{background:var(--footer-base);height:58px;display:flex;flex-direction:column;align-items:center;justify-content:center;font-size:7.3px;color:#e6e1dc;line-height:12.6px}
</style>
</head>
<body>
<div class="style-switcher" aria-hidden="true">
  <span style="background:#7a7876"></span>
  <span style="background:var(--orange)"></span>
  <span style="background:#5e5c5a"></span>
  <span style="background:#eeeae6"></span>
  <span style="background:#454443"></span>
</div>

<header class="site-header">
  <div class="brand-pre">LAW OFFICES OF</div>
  <div class="brand-name">DORIAN VASKE <em>PLLC</em></div>
  <div class="header-contact">
    <div><b>PHONE:</b>(555) 014-2290</div>
    <div><b>EMAIL:</b>Dorian@DorianVaskeLaw.example</div>
  </div>
</header>

<div class="page">
  <nav class="main-nav">
    <a href="#">Home</a><a href="#">Contact Me</a><a href="#">Criminal Law</a><a href="#" class="is-active">Family Law</a><a href="#">Will Drafting</a><a href="#">Attorney Profile</a><a href="#">Fees</a><a href="#">Legal Updates</a><a href="#">Online Resources</a><a href="#">Articles</a>
  </nav>

  <section class="hero">
    <svg width="549" height="229" viewBox="0 0 549 229">
      <defs>
        <linearGradient id="heroPhoto" x1="0" y1="0" x2="1" y2="1">
          <stop offset="0" stop-color="#b8876a"/>
          <stop offset=".5" stop-color="#d9b79c"/>
          <stop offset="1" stop-color="#8f5a3f"/>
        </linearGradient>
        <linearGradient id="heroOrange" x1="0" y1="0" x2="1" y2="1">
          <stop offset="0" stop-color="#e04f10"/>
          <stop offset="1" stop-color="#f27a30"/>
        </linearGradient>
      </defs>
      <rect width="549" height="229" fill="url(#heroPhoto)" role="img" aria-label="Portrait of the attorney smiling in an office hallway"/>
      <polygon points="336,0 549,0 549,229 303,229" fill="url(#heroOrange)"/>
    </svg>
    <div class="hero-title">
      <div class="lead">SPECIALIZING IN</div>
      <div class="main">CRIMINAL DEFENSE<br>AND FAMILY LAW</div>
    </div>
  </section>

  <div class="tagline">Practice focused on accomplishing your goals<br>through results-oriented work at a discount price</div>

  <section class="features">
    <article class="feature">
      <h2>Personal Attention.</h2>
      <svg class="thumb" role="img" aria-label="Folder tab labelled legal in a filing drawer"><defs><linearGradient id="t1" x1="0" x2="1"><stop offset="0" stop-color="#d9a35a"/><stop offset="1" stop-color="#9c6a3a"/></linearGradient></defs><rect width="160" height="75" fill="url(#t1)"/></svg>
      <p>I control the size of my practice so that I am able to devote 100% of my effort to each case. I have no “associates” so I handle every case personally.</p>
    </article>
    <article class="feature">
      <h2>General Practice</h2>
      <svg class="thumb" role="img" aria-label="Judge's gavel in front of a flag"><defs><linearGradient id="t2" x1="0" x2="1"><stop offset="0" stop-color="#3b4f8a"/><stop offset=".6" stop-color="#c23a3a"/><stop offset="1" stop-color="#e8d8d0"/></linearGradient></defs><rect width="160" height="75" fill="url(#t2)"/></svg>
      <p>I am available to provide your defense if you are accused of a felony or misdemeanor. Additionally, I can work with you on family matters such as divorce, child custody, wills, and nuptial agreements.</p>
    </article>
    <article class="feature">
      <h2>Free first consulatation</h2>
      <svg class="thumb" role="img" aria-label="Lawyer meeting with a couple in a bright office"><defs><linearGradient id="t3" x1="0" x2="1"><stop offset="0" stop-color="#e9eef0"/><stop offset="1" stop-color="#b8bcc0"/></linearGradient></defs><rect width="160" height="75" fill="url(#t3)"/></svg>
      <p>I will take time to listen to your individual situation. I will explain the legal issues, and the risks involved in each course of action we may pursue so that you can make informed decisions about how to proceed.</p>
    </article>
  </section>

  <section class="content">
    <div class="areas">
      <h2 class="section-title">Areas of specialization</h2>
      <div class="area">
        <h3>CRIMINAL LAW</h3>
        <p>Convictions carry serious consequences and can often have a negative financial impact as well as putting your freedom in jeopardy. I know how to work on your behalf because I used to work at the Harlow County Attorney’s Office and appeared on the prosecution’s behalf for more than 600 cases. I will prepare your defense, negotiate plea bargains if desired, or take the case to trial.</p>
      </div>
      <div class="area">
        <h3>EXPERIENCE MATTERS</h3>
        <p>Every case is different. You can take comfort knowing that I have appeared in court on a wide variety of cases including assault, drug possession and distribution, DWI, disorderly conduct, theft, burglary, domestic assault, check forgery, violations or orders for protection, firearms violations and DWI test refusals. I am also prepared to handle your probation violation or expungement.</p>
      </div>
      <div class="area">
        <h3>FAMILY LAW</h3>
        <p>I am prepared to handle your family law concerns. I can guide you through the process of child custody matters, divorce, wills and nuptial agreements to ensure that you receive a fair and equitable result on these sensitive matters.</p>
      </div>
    </div>
    <aside class="updates">
      <h2 class="section-title">Latest Updates</h2>
      <div class="update"><h3>Duis autem vel eum iriure dolor.</h3><time>March, 27, 2012</time><p>Ut wisi enim ad minim veniam, quis nostrud exerci tation ullamcorper suscipit lobortis nisl ut aliquip ex ea commodo consequat.</p></div>
      <div class="update"><h3>Duis autem vel eum iriure dolor.</h3><time>March, 27, 2012</time><p>Ut wisi enim ad minim veniam, quis nostrud exerci tation ullamcorper suscipit lobortis nisl ut aliquip ex ea commodo consequat.</p></div>
      <div class="update"><h3>Duis autem vel eum iriure dolor.</h3><time>March, 27, 2012</time><p>Ut wisi enim ad minim veniam, quis nostrud exerci tation ullamcorper suscipit lobortis nisl ut aliquip ex ea commodo consequat.</p></div>
    </aside>
  </section>

  <footer>
    <div class="site-footer">
      <div class="footer-col">
        <h2>About Me</h2>
        <p>My practice is focused on accomplishing your goals through results-oriented work at a discount price. For your convenience, I handle legal matters throughout the Twin Cities, including Harlow, Brennick, Aldmoor, and Wexford counties. I understand that legal issues can appear complicated, and that is why I take a hands-on approach to guiding you through your legal needs.</p>
      </div>
      <div class="footer-col">
        <h2>Subscribe</h2>
        <p>Enter your email address to receive notifications of legal updates by e-mail.</p>
        <div class="subscribe-form"><span class="field">Enter email here</span><span class="btn">Submit</span></div>
      </div>
      <div class="footer-col">
        <h2>Contact Me</h2>
        <p>Looking for legal representation? I offer Free consultation. You can contact me via any of the following option.</p>
        <p style="margin-top:12px">Phone: 555 014 2290<br>Email : dorian@dorianvaskelaw.example</p>
      </div>
    </div>
    <div class="footer-base">
      <div>dorianvaskelaw.example © 2012 Law Offices of Dorian Vaske PLLC</div>
      <div>Delivering legal services in the greater Twin Cities area.</div>
    </div>
  </footer>
</div>
</body>
</html>
```